Staff Newsletter Template Image

We are looking for two .jpg images that we can put into a Word document and use for our staff newsletter. We will then add content using text boxes.
Attached is the current template which works for the columns and size that we need but we just want a fresh new design.
The Word document shows how we use it.
The name will stay the same - Team upBeat but can be a different look to the current one.

Target Market(s)

Sales team

Colors

Designer to choose colors to be used in the design.

Requirements
Must have
• Colours will be green, grey and white, possibly cream if needed. All from the guidelines.
• I have attached our brand guidelines which shows design elements and fonts for our brand. Also attached is brand guidelines for one of our product lines as we would like to use the same green.
• It needs to be nice to look at and motivational for our team

```html
<!DOCTYPE html>
<html lang="en">
<head>
<meta charset="utf-8">
<title>Team upBeat Newsletter</title>
<link href="https://fonts.googleapis.com/css2?family=Arimo:wght@400;700&family=Open+Sans:wght@400;600&display=swap" rel="stylesheet">
<style>
:root{
  --page-bg:#f2f2f0;
  --paper:#ffffff;
  --green:#3f7f22;
  --green-link:#4f9a2a;
  --green-light:#a9d27a;
  --green-mid:#6fae3d;
  --green-dark:#2f6a18;
  --brand-grey:#5e5e5e;
  --text:#555555;
  --text-dark:#444444;
  --muted:#8a8a8a;
  --rule:#c9c9c9;
  --bar:#e6e6e6;
  --placeholder:#dcdddb;
}
*{box-sizing:border-box;margin:0;padding:0}
html,body{width:743px;height:1200px;overflow:hidden}
body{background:var(--page-bg);font-family:"Arimo",Arial,sans-serif;color:var(--text);position:relative}
.preheader{position:absolute;left:0;top:0;width:743px;height:57px;background:var(--paper);text-align:center;font-size:11px;line-height:14px;color:var(--muted);padding-top:9px}
.preheader a{color:var(--green-link);font-weight:700;text-decoration:underline}
.page{position:absolute;left:17px;top:57px;width:708px;height:1143px;background:var(--paper)}
.masthead{position:relative;height:152px;background:linear-gradient(180deg,var(--green-light) 0%,var(--green-mid) 50%,var(--green) 100%)}
.masthead-band{position:absolute;left:0;bottom:0;width:100%;height:14px;background:var(--green-dark)}
.brand-panel{position:absolute;left:0;top:10px;width:360px;height:128px;background:var(--paper);clip-path:polygon(0 0,100% 0,88% 100%,0 100%)}
.brand-name{position:absolute;left:18px;top:42px;display:flex;align-items:center;gap:12px;font-weight:700;font-size:34px;color:var(--brand-grey);letter-spacing:.5px}
.brand-dot{width:22px;height:22px;border-radius:50%;background:var(--green-mid)}
.masthead-title{position:absolute;left:366px;top:48px;font-family:"Open Sans",Arial,sans-serif;font-weight:600;font-size:45px;color:#fff;letter-spacing:1px}
.issue-bar{margin:0 12px;background:var(--bar);padding:12px 12px 13px}
.issue-bar-inner{background:var(--paper);height:26px;display:flex;justify-content:space-between;align-items:center;padding:0 10px;font-size:13px;color:var(--green)}
.columns{display:flex;justify-content:space-between;padding:10px 12px 0 13px;height:680px}
.col-left{width:300px}
.col-right{width:370px}
.label{font-size:15px;font-weight:700;color:var(--green);margin-bottom:4px}
.label.dark{color:var(--text-dark)}
.toc{list-style:none}
.toc li{font-size:14.5px;line-height:24px;padding-left:12px;position:relative}
.toc li::before{content:"";position:absolute;left:1px;top:10px;width:4px;height:4px;border-radius:50%;background:var(--green-link)}
.toc a{color:var(--text);text-decoration:none;border-bottom:1px solid var(--text)}
.divider{border:0;border-top:1px dotted var(--rule);margin:10px 0}
.side-story h2{font-size:15.5px;font-weight:700;color:var(--green);text-decoration:underline;margin:8px 0 3px}
.side-story p{font-size:14.5px;line-height:20.5px;padding-bottom:4px}
.story{padding:0 0 6px}
.story h2{font-size:15.5px;font-weight:700;color:var(--text);line-height:20px;margin:0 0 4px}
.story p{font-size:14.5px;line-height:20.5px}
.read-more{display:inline-block;font-size:11.5px;letter-spacing:.5px;color:var(--green);text-decoration:none;border-bottom:1px solid var(--green);margin-top:3px}
.story-media{display:flex;gap:8px}
.thumb{flex:0 0 107px;height:103px;background:var(--placeholder)}
.col-right .divider{margin:16px 0}
.footer-links{margin:0 12px;border-top:1px dotted var(--rule);border-bottom:1px dotted var(--rule);display:flex;height:124px;padding-top:16px}
.footer-block{width:50%;padding:0 12px}
.footer-block + .footer-block{border-left:1px dotted var(--rule);padding-left:20px;height:84px}
.footer-block h3{font-size:16px;font-weight:700;color:var(--green);margin-bottom:8px}
.footer-body{display:flex;gap:8px;font-size:14.5px;line-height:20.5px}
.footer-body a{color:var(--green-link);text-decoration:underline}
.footer-body svg{flex:0 0 auto}
.icon-line{fill:none;stroke:var(--green);}
.legal{margin-top:16px;text-align:center;font-size:11px;line-height:13px;letter-spacing:.6px;color:var(--muted);padding:0 30px}
.legal a{color:var(--green-link);font-weight:700;text-decoration:underline}
</style>
</head>
<body>
<div class="preheader">
  <p>You're receiving this newsletter because you bought widgets from us.</p>
  <p>Having trouble reading this email? <a href="#">View it in your browser</a>. Not interested anymore? <a href="#">Unsubscribe Instantly</a>.</p>
</div>

<main class="page">
  <header class="masthead">
    <div class="brand-panel">
      <div class="brand-name"><span class="brand-dot"></span>Team upBeat</div>
    </div>
    <div class="masthead-title">NEWSLETTER</div>
    <div class="masthead-band"></div>
  </header>

  <div class="issue-bar">
    <div class="issue-bar-inner"><span>Friday&nbsp; 20 August</span><span>ISSUE 9</span></div>
  </div>

  <div class="columns">
    <aside class="col-left">
      <p class="label">In this Issue:</p>
      <ul class="toc">
        <li><a href="#">Lorem ipsum dolor sit amet</a></li>
        <li><a href="#">Consectetur adipiscing elit.</a></li>
        <li><a href="#">Suspendisse et nisl sem.</a></li>
        <li><a href="#">At luctus metus.&nbsp;</a></li>
      </ul>
      <hr class="divider">
      <section class="side-story">
        <h2>Amet dolor sit vitae leo</h2>
        <p>Lorem ipsum dolor sit amet, consectetur adipiscing elit. Suspendisse et nisl sem, at luctus metus. Morbi congue cursus ligula, sit amet iaculis leo bibendum vitae.</p>
      </section>
      <hr class="divider">
      <section class="side-story">
        <h2>Luxtus cras morbi</h2>
        <p>Lorem ipsum dolor sit amet, consectetur adipiscing elit. Suspendisse et nisl sem, at luctus metus.</p>
      </section>
      <hr class="divider">
      <section class="side-story">
        <h2>Ligula dolor leo luctus</h2>
        <p>Lorem ipsum dolor sit amet, consectetur adipiscing elit. Suspendisse et nisl sem, at luctus metus.</p>
      </section>
      <hr class="divider">
      <p class="label dark">More Articles</p>
      <ul class="toc">
        <li><a href="#">Lorem ipsum dolor sit amet</a></li>
        <li><a href="#">Consectetur adipiscing elit.</a></li>
        <li><a href="#">Suspendisse et nisl sem.</a></li>
        <li><a href="#">At luctus metus.&nbsp;</a></li>
      </ul>
    </aside>

    <div class="col-right">
      <article class="story">
        <h2>Lorem ipsum dolor sit amet, consectetur adipiscing elit</h2>
        <div class="story-media">
          <div class="thumb" role="img" aria-label="Article photo"></div>
          <div>
            <p>Lorem ipsum dolor sit amet, consectetur adipiscing elit. Suspendisse et nisl sem, at luctus metus.</p>
            <a class="read-more" href="#">READ MORE</a>
          </div>
        </div>
      </article>
      <hr class="divider">
      <article class="story">
        <h2>Amet sit iaculus leo bibendum viate quis mauris</h2>
        <p>Lorem ipsum dolor sit amet, consectetur adipiscing elit. Suspendisse et nisl sem, at luctus metus. Morbi congue cursus ligula, sit amet iaculis leo bibendum vitae.</p>
        <a class="read-more" href="#">READ MORE</a>
      </article>
      <hr class="divider" style="margin:8px 0 12px">
      <article class="story">
        <h2>Luctus cras et enim odio et triquse elit</h2>
        <p>Lorem ipsum dolor sit amet, consectetur adipiscing elit. Suspendisse et nisl sem, at luctus metus. Morbi congue cursus ligula, sit amet iaculis leo bibendum vitae..</p>
        <a class="read-more" href="#">READ MORE</a>
      </article>
      <hr class="divider" style="margin:14px 0 22px">
      <article class="story">
        <h2>Morbi conque ligula iaculis fuscue</h2>
        <p>Lorem ipsum dolor sit amet, consectetur adipiscing elit. Suspendisse et nisl sem, at luctus metus. Morbi congue cursus ligula, sit amet iaculis leo bibendum vitae.</p>
        <a class="read-more" href="#">READ MORE</a>
      </article>
    </div>
  </div>

  <footer>
    <div class="footer-links">
      <div class="footer-block">
        <h3>Forward to Friend</h3>
        <div class="footer-body">
          <svg width="56" height="42" viewBox="0 0 56 42" aria-hidden="true"><rect class="icon-line" x="2" y="2" width="52" height="38" stroke-width="3"/><path class="icon-line" d="M2 2 L28 24 L54 2 M2 40 L22 19 M54 40 L34 19" stroke-width="3"/></svg>
          <p>Suspendisse et nisl sem, at luctus metus. <a href="#">Morbi congue cursus ligula</a></p>
        </div>
      </div>
      <div class="footer-block">
        <h3>Unsubscribe</h3>
        <div class="footer-body">
          <svg width="44" height="44" viewBox="0 0 44 44" aria-hidden="true"><circle class="icon-line" cx="22" cy="22" r="17" stroke-width="5"/><line class="icon-line" x1="10" y1="10" x2="34" y2="34" stroke-width="5"/></svg>
          <p>Suspendisse et nisl sem, at luctus metus. <a href="#">Morbi congue cursus ligula</a></p>
        </div>
      </div>
    </div>
    <p class="legal">LOREM IPSUM DOLOR SIT AMET, CONSECTETUR ADIPISCING ELIT. FUSCE PULVINAR, EROS TRISTIQUE HENDRERIT TEMPOR, IPSUM MAURIS TRISTIQUE METUS, IN LUCTUS ENIM MASSA AT DIAM. SED EU AUGUE EROS. DUIS SED VELIT AC <a href="#">RISUS MOLLIS MOLESTIE.</a></p>
  </footer>
</main>
</body>
</html>
```